Web Design Project

I need a three page website. I have designed the index.html and the specialevent.html page.

I need someone to finetune the pages for me.

Where I have difficulty is with the following:
I want to add an event table driven by php database.
The administrator of the event will login and create the wording that fits under each colmn. The administrator the submit the form to php database. The database then display in a html.

The Table contains 5 coloums and the rows can vary and can go up to as many as 100.

The table set out events on a program
In the last column of every row I need a submit button to "View and Book" I need to link those buttons with external links/pages.

I use Dreamweaver CS5 and I need to have it in this format in order for me to edit it in the future.

The Table needs to be updated once a year for this program. So ideally if someone has a password to update the certain regions this is what I have in mind.

I have also designed a mockup of the restaurant page. At the top I need.
1) 4 Colapsable panels
a) Restaurants - opening the names of the restaurants
b) Coffee shops and light lunches .... with the names
c) Family
d) Home eateries

From the colapsable panel of each of these I need a anchored link to the description/photos of each...with a BOOK now button I can submit bookings to.

I added a colapsable panel in each restaurants description to keep everything contained.

Please help

• Background must be fixed so that main.div scroll over it

The colours are chosen so please stick to it.

The green for the submit button I short is. #C8D707

I need to edit the pages in Dreamweaver CS5. /Flexilayout2pro

Please ask if you need to know anything. I exactly know what I want.

Kind regards
Marius Delport

The colours are fine.

The wording " lindekloofdirect BOOKING agent" should appear right at the top in the white horizon part of the background image.

The specialevent page I described already. I am interested in the editable solution. for this.

I will make up a mockup of the third page and send it later.

Regards

```html
<!DOCTYPE html>
<html lang="en">
<head>
<meta charset="utf-8">
<title>Lindekloof Online Booking agent</title>
<link rel="stylesheet" href="https://fonts.googleapis.com/css2?family=Source+Sans+3:wght@300;400;600&display=swap">
<style>
:root{
  --lime:#c8d707;
  --lime-light:#e4ee5a;
  --lime-pale:#f0f4b0;
  --olive:#4a4a0e;
  --olive-text:#3b3a12;
  --night:#33322d;
  --ink:#1f1f12;
  --grey-text:#9a9a9a;
  --rule:#dcdcdc;
  --white:#ffffff;
  --stay:#f2591c;
  --play:#fdf99a;
  --eat:#45b6ef;
}
*{box-sizing:border-box;margin:0;padding:0}
html,body{width:1200px;height:2161px;overflow:hidden}
body{background:var(--night);font-family:"Source Sans 3",sans-serif;position:relative;color:var(--ink)}
.hero{position:absolute;left:0;top:0;width:1200px;height:663px;
  background:linear-gradient(180deg,#e6e6e2 0%,#8a8a84 12%,#6f6f66 30%,#5a5a52 48%,#7d7d76 68%,#9a9a93 85%,#6c6c66 100%)}
.site-title{position:absolute;left:104px;top:68px;font-size:45px;font-weight:600;color:var(--white);letter-spacing:-.3px}
.site-title .place{color:var(--lime)}
.main-nav{position:absolute;left:98px;top:143px;width:1002px;height:56px;border-radius:8px;
  background:linear-gradient(180deg,#e3ee3c 0%,var(--lime) 55%,#a9b604 100%);
  box-shadow:0 3px 6px rgba(0,0,0,.35);display:flex;justify-content:center}
.main-nav a{display:block;padding:0 34px;line-height:56px;font-size:21px;color:var(--ink);text-decoration:none;border-left:1px solid rgba(80,85,0,.35)}
.main-nav a:first-child{border-left:none}
.slider-dots{position:absolute;left:560px;top:579px;display:flex;gap:6px}
.slider-dots span{width:11px;height:11px;border-radius:50%;background:rgba(255,255,255,.35)}
.slider-dots span.active{background:var(--lime)}
.page{position:absolute;left:101px;top:622px;width:998px;height:1160px;background:var(--white);border-radius:22px 22px 0 0}
.intro-title{position:absolute;left:0;width:100%;top:18px;text-align:center;font-size:39px;font-weight:400;color:var(--olive-text)}
.services{position:absolute;left:53px;top:91px;display:flex;gap:23px}
.service{width:285px;height:305px;background:var(--olive);border-radius:10px;padding:17px 19px 0;text-align:center}
.service-btn{height:125px;border-radius:9px;display:flex;align-items:center;justify-content:center;font-size:40px;box-shadow:inset 0 -8px 14px rgba(0,0,0,.12)}
.service-btn .pre{font-size:32px}
.stay{background:linear-gradient(180deg,#fb7a3a,var(--stay) 60%,#e4410e);color:var(--white)}
.stay .main{color:var(--ink)}
.play{background:var(--play);color:var(--ink)}
.play .pre{color:#b3b710}
.eat{background:linear-gradient(180deg,#71caf5,var(--eat));color:var(--ink)}
.eat .pre{color:var(--white)}
.service p{color:var(--white);font-size:14px;line-height:26px;margin-top:20px;padding:0 18px}
.events-title{position:absolute;left:62px;top:490px;font-size:30px;font-weight:300;color:var(--ink)}
.events-rule{position:absolute;left:30px;top:542px;width:938px;height:14px;background:linear-gradient(180deg,rgba(0,0,0,.05),rgba(0,0,0,0));border-radius:50%}
.event{position:absolute;left:50px;width:840px;height:160px}
.event-date{position:absolute;left:0;top:0;width:75px;height:75px;border-radius:8px;background:linear-gradient(180deg,#dbe63a,var(--lime));box-shadow:0 2px 0 #98a305;text-align:center;color:var(--white)}
.event-date .day{display:block;font-size:28px;font-weight:600;line-height:30px;margin-top:9px}
.event-date .month{display:block;font-size:18px;line-height:20px;color:var(--olive-text)}
.event h3{position:absolute;left:91px;top:-1px;font-size:24px;font-weight:400;color:var(--ink)}
.event p{position:absolute;left:92px;top:36px;width:728px;font-size:13.5px;line-height:21.6px;color:var(--grey-text)}
.read-more{position:absolute;left:92px;top:105px;width:95px;height:32px;border-radius:16px;background:var(--ink);color:var(--white);font-size:13px;line-height:32px;text-align:center}
.event-rule{position:absolute;left:50px;width:837px;height:1px;background:var(--rule)}
.site-footer{position:absolute;left:101px;top:1769px;width:998px;height:279px;border-radius:14px 14px 40px 40px / 14px 14px 14px 14px;
  background:linear-gradient(180deg,var(--lime-pale) 0 8px,#d7e32e 8px,var(--lime) 40%,#c3d104 100%);box-shadow:0 3px 0 #a4b004}
.footer-col{position:absolute;top:52px;height:120px}
.footer-col h4{font-size:23px;font-weight:400;color:var(--ink);margin-bottom:6px}
.footer-col p,.footer-col li{font-size:13px;line-height:24px;color:var(--olive-text);list-style:none}
.footer-col .phone{font-size:17px;color:var(--ink)}
.col-contact{left:49px}
.col-services{left:302px}
.col-news{left:517px}
.col-touch{left:782px}
.col-services h4,.col-news h4,.col-touch h4{margin-bottom:0}
.footer-sep{position:absolute;top:54px;width:1px;height:138px;background:rgba(80,85,0,.25)}
.email-field{width:212px;height:27px;border-radius:14px;background:var(--white);font-size:11px;line-height:27px;padding-left:15px;color:#b5b5b5;margin-top:4px}
.subscribe{margin:8px 0 0 126px;width:88px;height:28px;border-radius:14px;background:var(--lime-pale);font-size:14px;line-height:28px;text-align:center;color:var(--ink)}
.social{display:flex;gap:5px;margin-top:2px}
.social span{width:29px;height:29px;border-radius:50%;background:var(--ink)}
.copyright{position:absolute;left:0;width:1200px;top:2080px;text-align:center;font-size:13px;color:#8e8e86}
</style>
</head>
<body>
<div class="hero" role="img" aria-label="Black and white photograph of a small Karoo town with a church spire, trees and mountains behind"></div>
<h1 class="site-title"><span class="place">Lindekloof</span> Online Booking agent</h1>
<nav class="main-nav">
  <a href="#">Home</a><a href="#">Accommodation</a><a href="#">Play</a><a href="#">Contact</a>
</nav>
<div class="slider-dots"><span class="active"></span><span></span><span></span><span></span><span></span></div>

<main class="page">
  <h2 class="intro-title">Your booking agent for</h2>
  <section class="services">
    <div class="service">
      <div class="service-btn stay"><span class="pre">book</span><span class="main">Stay</span></div>
      <p>Find the perfect accommodation to suit your specific needs. Click on bookStay to view and book our properties online NOW!</p>
    </div>
    <div class="service">
      <div class="service-btn play"><span class="pre">book</span><span class="main">Play</span></div>
      <p style="margin-top:10px">Secure your playlist Lindekloof has wonderful excursions, activities, shows and festivals on offer. Click on bookPlay and book it all ONLINE!</p>
    </div>
    <div class="service">
      <div class="service-btn eat"><span class="pre">book</span><span class="main">Eat</span></div>
      <p>Wow! Book your eating experience with us. As always Lindekloof has the best on offer to enhance your cullinary experience. Click bookEat!</p>
    </div>
  </section>

  <h2 class="events-title">Special Event and Festivals</h2>
  <div class="events-rule"></div>

  <article class="event" style="top:595px">
    <div class="event-date"><span class="day">01</span><span class="month">April</span></div>
    <h3>Olive Festival - April 2014</h3>
    <p>Vivamus porttitor, g, purus nisi eleifend libero, a tempus libero lectus feugiat felis. Morbi diam mauris, viverra in, gravida eu, attis in, ante. Morbi eget arcu. Morbi porta, libero id ullamcorper nonummy, nibh ligula pulvinar metus, eget consectetuer augue nisi quis lacus.</p>
    <div class="read-more">Read More</div>
  </article>
  <div class="event-rule" style="top:755px"></div>

  <article class="event" style="top:783px">
    <div class="event-date"><span class="day">02</span><span class="month">Aug</span></div>
    <h3>Winter School - August 2014</h3>
    <p>Vivamus porttitor, g, purus nisi eleifend libero, a tempus libero lectus feugiat felis. Morbi diam mauris, viverra in, gravida eu, attis in, ante. Morbi eget arcu. Morbi porta, libero id ullamcorper nonummy, nibh ligula pulvinar metus, eget consectetuer augue nisi quis lacus.</p>
    <div class="read-more">Read More</div>
  </article>
  <div class="event-rule" style="top:941px"></div>

  <article class="event" style="top:963px">
    <div class="event-date"><span class="day">03</span><span class="month">Sep</span></div>
    <h3>Donec scelerisque leo - September 2014</h3>
    <p>Vivamus porttitor, g, purus nisi eleifend libero, a tempus libero lectus feugiat felis. Morbi diam mauris, viverra in, gravida eu, attis in, ante. Morbi eget arcu. Morbi porta, libero id ullamcorper nonummy, nibh ligula pulvinar metus, eget consectetuer augue nisi quis lacus.</p>
    <div class="read-more">Read More</div>
  </article>
</main>

<footer class="site-footer">
  <div class="footer-col col-contact">
    <h4>Contact Us</h4>
    <p class="phone">0861 272 727</p>
    <p>email: admin@lindekloofdirect.biz</p>
    <p>address: Mill Street, Lindekloof</p>
  </div>
  <div class="footer-sep" style="left:276px"></div>
  <div class="footer-col col-services">
    <h4>Services List</h4>
    <ul><li>Business Directory</li><li>Relevant links and websites</li><li>Emergency Numbers</li></ul>
  </div>
  <div class="footer-sep" style="left:485px"></div>
  <div class="footer-col col-news">
    <h4>Newsletter Sign Up</h4>
    <p>Please sign up here for latest news</p>
    <div class="email-field">email address</div>
    <div class="subscribe">Subscribe</div>
  </div>
  <div class="footer-sep" style="left:752px"></div>
  <div class="footer-col col-touch">
    <h4>Get in Touch</h4>
    <div class="social"><span></span><span></span><span></span><span></span></div>
  </div>
</footer>
<p class="copyright">Copyright © 2013 Company Name.&nbsp; All right reserved.</p>
</body>
</html>
```